Business Card Design Project

Marla's Elixirs is a natural skincare business and we need a business card designed. The company focuses on natural products and will be launching with body scrubs and bath fizzies and our mission statement is: To deliver high quality natural beauty products at a good value. It's two cards - one design - the only information changing would be name and email address

Target Market(s)

Females ages 20-50

Industry/Entity Type

Business

Requirements
Must have
• Marla's Elixirs

Yvonne Hart-Becker
T: 800-555-7341
E: Yvonne@MarlasElixirs-example.com
W: www.MarlasElixirs-example.com

Tobias Werner
T: 800-555-7341
E: Tobias@MarlasElixirs-example.com
W: www.MarlasElixirs-example.com
Nice to have
• I'd like to use the colors or text found at www.marlaselixirs-example.com but I'm open to suggestions since design isn't set in stone yet. I would also like to have the words .....a little bit of magic somewhere under the company name in a different type of font. I would like a design that feels clean and maybe a retro feel to it - front and back would be nice but not mandatory

```html
<!DOCTYPE html>
<html lang="en">
<head>
<meta charset="utf-8">
<title>Marla's Elixirs – Business Card</title>
<link rel="stylesheet" href="https://fonts.googleapis.com/css2?family=Montserrat:wght@700&family=PT+Sans:wght@400&display=swap">
<style>
  :root {
    --frame-plum: #984577;
    --card-white: #ffffff;
    --brand-purple: #8e2a85;
    --name-ink: #231f20;
    --phone-plum: #984577;
    --email-grey: #8a8a8c;
    --web-blue: #1a90d2;
  }
  * { margin: 0; padding: 0; box-sizing: border-box; }
  html, body {
    width: 1200px;
    height: 707px;
    overflow: hidden;
    background: var(--frame-plum);
  }
  .business-card {
    position: relative;
    width: 1200px;
    height: 707px;
    background: var(--frame-plum);
  }
  .card-face {
    position: absolute;
    left: 51px;
    top: 51px;
    width: 1098px;
    height: 604px;
    background: var(--card-white);
    text-align: center;
    font-family: "PT Sans", "Myriad Pro", Arial, sans-serif;
  }
  .brand-name {
    position: absolute;
    top: 68px;
    left: 0;
    width: 100%;
    font-size: 60px;
    line-height: 1;
    color: var(--brand-purple);
    letter-spacing: 0.5px;
  }
  .person-name {
    position: absolute;
    top: 262px;
    left: 0;
    width: 100%;
    font-family: "Montserrat", "Century Gothic", sans-serif;
    font-weight: 700;
    font-size: 52px;
    line-height: 1;
    color: var(--name-ink);
  }
  .contact-list {
    position: absolute;
    top: 408px;
    left: 0;
    width: 100%;
    list-style: none;
    font-size: 48px;
    line-height: 65px;
  }
  .contact-phone { color: var(--phone-plum); }
  .contact-email { color: var(--email-grey); }
  .contact-web { color: var(--web-blue); }
</style>
</head>
<body>
  <main class="business-card">
    <section class="card-face">
      <h1 class="brand-name">Marla's Elixirs</h1>
      <h2 class="person-name">Yvonne Hart-Becker</h2>
      <ul class="contact-list">
        <li class="contact-phone">Telephone: 800-555-7341</li>
        <li class="contact-email">E-Mail: Yvonne@MarlasElixirs-example.com</li>
        <li class="contact-web">www.MarlasElixirs-example.com</li>
      </ul>
    </section>
  </main>
</body>
</html>
```